New solo practice law firm is looking for an elegant, professional, and interactive web design

I need a web design and developer for a new small law firm in Sacramento, California called Dorian Kessly Law, A Professional Corporation. I am a trial lawyer who represents average people facing difficult litigation disputes, including criminal defense as a former prosecutor and civil litigation as a civil litigator. Criminal defense includes domestic violence, battery, assault, drug possession, theft, DUI, etc. Civil litigation includes business disputes, property disputes, employment disputes, family law disputes, and immigration issues. I would like to see web designs that incorporate my logo and use the logo's navy blue and gold colors. I have uploaded the files of my logo to this brief. Please only use the navy blue and gold version. Overall, I want the design to look firm, professional, and elegant.

I plan on having the following pages on my website: (1) Home, (2) Dorian Kessly, (3) Practice Areas, (4) Insights, (5) Contact. I've hand drawn a preliminary sketch concept of what I envision the home page's layout to look like (attached with a text version). I would like your design to keep a similar layout for the homepage and incorporate my logo's colors within it but I am open to creative layout alternatives/ideas. I would like the other pages to have a similar look and feel as the home page. Some of the areas currently in my sketch do not have the full text. You can insert other text for now and I will provide the winner the full text.

In terms of the pictures on the website, I enjoy images of courthouses, columns (example attached but I cannot use this one), and, if possible, images from Sacramento, CA in my background (headshot attached). A plus would be live images that move and also sections of the webpage moving in the viewers view as they scroll down on the page. Also, it would be great to have my logo act as the tab for the website. I can provide other versions of the logo if needed.

I look forward to seeing your Wordpress designs!

People needing legal representation.

Law

Coded - Design and coding required

5+ page

Serif

• Incorporate my logo and my logo's colors.
• Live pictures and images appearing as viewers scroll on page.

```html
<!DOCTYPE html>
<html lang="en">
<head>
<meta charset="utf-8">
<title>Dorian Kessly Law</title>
<link href="https://fonts.googleapis.com/css2?family=Playfair+Display:wght@700&family=Poppins:wght@400;500;600&display=swap" rel="stylesheet">
<style>
:root{
  --navy:#1b2846;
  --navy-deep:#1e2640;
  --navy-mid:#262d48;
  --panel:#1c2b4c;
  --gold:#b39b63;
  --gold-light:#c9ae6e;
  --white:#ffffff;
  --ink:#2b2f3a;
  --muted:#c3c7d3;
}
*{margin:0;padding:0;box-sizing:border-box}
html,body{width:1200px;height:3361px;overflow:hidden}
body{position:relative;font-family:"Poppins",sans-serif;color:var(--white);background:var(--white)}
.abs{position:absolute}
.serif{font-family:"Playfair Display",serif;font-weight:700}
.gold{color:var(--gold)}

/* header */
.topbar{left:0;top:0;width:1200px;height:107px;background:var(--navy)}
.brand{left:150px;top:24px;color:var(--gold);font-weight:500;letter-spacing:3px;font-size:19px;line-height:1;display:flex;align-items:center;gap:12px}
.brand small{display:block;font-size:10px;letter-spacing:3px;margin-top:6px;padding-left:24px}
.brand-dot{display:block;width:58px;height:58px;border:2px solid var(--gold);flex:none}
.head-info{top:42px;display:flex;gap:10px;font-size:11px;line-height:15px}
.head-info b{font-family:"Playfair Display",serif;font-weight:400;font-size:13px;display:block}
.ring{width:30px;height:30px;border:1px solid var(--muted);border-radius:50%;display:flex;align-items:center;justify-content:center;flex:none}
.head-sep{left:813px;top:42px;width:1px;height:38px;background:var(--muted)}
.nav{left:149px;top:108px;width:902px;height:55px;background:var(--white);display:flex;justify-content:center;align-items:center;font-size:12px;color:var(--ink);z-index:3}
.nav a{color:var(--ink);text-decoration:none;padding:0 21px;border-right:1px solid #e1e1e1;line-height:14px}
.nav a:last-child{border:none}
.nav a.active{color:var(--gold)}

/* hero */
.hero{left:0;top:134px;width:1200px;height:501px;background:linear-gradient(100deg,#2c2f35 0%,#4a4c50 35%,#3c3d40 60%,#26272a 100%)}
.hero-shade{left:0;top:134px;width:1200px;height:501px;background:rgba(20,22,30,.35)}
.hero-title{left:0;top:282px;width:1200px;text-align:center;font-size:60px;line-height:1}
.hero-line{top:314px;width:66px;height:3px;background:var(--white)}
.hero-sub{left:0;top:356px;width:1200px;text-align:center;font-size:17px}
.hero-text{left:0;top:393px;width:1200px;text-align:center;font-size:13px;line-height:22px}
.btn-gold{background:var(--gold);color:var(--white);font-size:11px;font-weight:500;text-align:center}
.hero-btn{left:497px;top:450px;width:205px;height:29px;line-height:22px}
.hero-arrow{top:392px;color:var(--white);font-size:20px}

/* about */
.label{font-size:10px;font-weight:500;color:var(--gold);text-transform:uppercase;text-align:center;width:1200px;left:0}
.about-title{left:0;top:753px;width:1200px;text-align:center;font-size:27px;color:var(--navy)}
.about-text{left:190px;top:797px;width:820px;text-align:center;font-size:10.5px;line-height:18.5px;color:var(--ink)}

/* cases */
.cases{left:0;top:934px;width:1200px;height:759px;background:radial-gradient(ellipse at 30% 30%,#2d3a5e 0%,#1e2846 55%,#161d33 100%)}
.cases-rule{left:0;top:1693px;width:1200px;height:1px;background:#4a5370}
.cases-title{left:0;top:1017px;width:1200px;text-align:center;font-size:28px;line-height:33px}
.divider{left:565px;top:1104px;width:70px;height:1px;background:#4a5370}
.card{width:257px;height:207px;background:rgba(28,36,60,.85);text-align:center}
.card svg{margin-top:28px}
.card h3{font-family:"Playfair Display",serif;font-weight:700;font-size:15px;margin-top:6px}
.card p{font-size:11px;line-height:19px;color:var(--muted);padding:6px 28px 0}
.card .more{font-size:10.5px;font-weight:600;margin-top:11px}
.photo-card{background:linear-gradient(135deg,#6e5a45,#3b3026 60%,#2a2420)}
.photo-card p{color:#e6e0d6}
.won-card{background:linear-gradient(120deg,#1d1d1f,#4a4036 55%,#8a7048)}

/* experience */
.exp{left:0;top:1693px;width:1200px;height:560px;background:linear-gradient(90deg,#2a3050 0%,#262d48 45%,#262d48 100%)}
.exp-fade{left:0;top:1693px;width:560px;height:560px;background:linear-gradient(160deg,rgba(70,76,100,.5),rgba(38,45,72,0) 60%)}
.band{left:0;top:2253px;width:1200px;height:121px;background:var(--gold)}
.exp-label{left:167px;top:1829px;font-size:10px;color:var(--gold);text-transform:uppercase}
.exp-title{left:167px;top:1847px;font-size:29px;line-height:37px}
.exp-text{left:167px;top:1932px;width:400px;font-size:11px;line-height:20px}
.ticks{font-size:11.5px;line-height:20px}
.ticks li{list-style:none;padding-left:16px;position:relative;margin-bottom:9px}
.ticks li::before{content:"";position:absolute;left:0;top:5px;width:8px;height:8px;border:2px solid var(--gold);border-radius:50%}
.portrait{left:690px;top:1780px;width:320px;height:594px;background:linear-gradient(180deg,#30375a 0%,#232838 55%,#18191f 100%)}

/* contact */
.contact-bg{left:0;top:2374px;width:1200px;height:446px;background:linear-gradient(180deg,#2a2218 0%,#1a1714 40%,#15151a 100%)}
.contact-panel{left:519px;top:2443px;width:681px;height:377px;background:var(--panel)}
.contact-label{left:123px;top:2528px;font-size:12px;font-weight:500}
.contact-title{left:123px;top:2551px;font-size:31px;line-height:42px}
.contact-text{left:123px;top:2645px;font-size:12px;line-height:22px}
.field{background:#f4f4f4;border:1px solid #d8d8d8;color:#9da2ad;font-size:11.5px;padding:12px 12px}
.submit{left:562px;top:2739px;width:245px;height:39px;line-height:39px;font-size:12px;font-weight:600}

/* footer */
.footer{left:0;top:2820px;width:1200px;height:541px;background:var(--navy-deep)}
.f-brand{left:152px;top:2872px;color:var(--gold);font-weight:500;letter-spacing:2.5px;font-size:14px;display:flex;align-items:center;gap:10px}
.f-brand small{display:block;font-size:7.5px;letter-spacing:2.5px;margin-top:4px;padding-left:18px}
.f-mark{display:block;width:40px;height:40px;border:2px solid var(--gold);flex:none}
.f-item{display:flex;gap:12px;font-size:11px;line-height:19px;color:var(--muted)}
.f-item b{color:var(--white);font-weight:400}
.f-head{font-size:18px}
.f-underline{width:24px;height:2px;background:var(--gold)}
.f-link{font-size:11px;color:var(--white)}
.f-link::before{content:"»";color:var(--gold);margin-right:5px}
.badge{left:196px;top:3144px;width:210px;height:46px;border:2px solid var(--gold);border-radius:23px}
.social{width:25px;height:25px;border:1px solid var(--white);border-radius:50%;top:3306px}
</style>
</head>
<body>

<!-- header -->
<div class="abs topbar"></div>
<div class="abs brand"><span class="brand-dot"></span><div>DORIAN KESSLY LAW<small>A PROFESSIONAL CORPORATION</small></div></div>
<div class="abs head-info" style="left:653px">
  <div class="ring"><svg width="13" height="13" viewBox="0 0 24 24" fill="none" stroke="#fff" stroke-width="2"><path d="M5 3h4l2 5-3 2a12 12 0 0 0 6 6l2-3 5 2v4a2 2 0 0 1-2 2A17 17 0 0 1 3 5a2 2 0 0 1 2-2z"/></svg></div>
  <div><b>+1-916-555-0148</b>Make a call</div>
</div>
<div class="abs head-sep"></div>
<div class="abs head-info" style="left:834px">
  <div class="ring"><svg width="13" height="13" viewBox="0 0 24 24" fill="none" stroke="#fff" stroke-width="2"><path d="M12 22s7-7 7-12a7 7 0 0 0-14 0c0 5 7 12 7 12z"/><circle cx="12" cy="10" r="2.5"/></svg></div>
  <div><b>Address</b>PO Box 4410, Sacramento, USA</div>
</div>
<nav class="abs nav">
  <a class="active">Home</a><a>Dorian Kessly</a><a>Practice Areas</a><a>Insights</a><a>Contact Us</a>
</nav>

<!-- hero -->
<div class="abs hero" role="img" aria-label="Photo of a lawyer at a desk with books and scales of justice"></div>
<div class="abs hero-shade"></div>
<div class="abs hero-line" style="left:271px"></div>
<div class="abs hero-line" style="left:863px"></div>
<h1 class="abs serif hero-title">The Best Defence</h1>
<div class="abs hero-sub">Personal Injury &nbsp;|&nbsp; Witness Assistance &nbsp;|&nbsp; Tax Criminal Law &nbsp;|&nbsp; General Law</div>
<p class="abs hero-text">We are a best law firm in family &amp; business industry. With more<br>than 15 years of experience in this area.</p>
<div class="abs btn-gold hero-btn">FREE CASE EVALUATION</div>
<div class="abs hero-arrow" style="left:31px">‹</div>
<div class="abs hero-arrow" style="left:1159px">›</div>

<!-- about -->
<div class="abs label" style="top:733px">About Us</div>
<h2 class="abs serif about-title">We Always Fight For Your Justice To Win</h2>
<p class="abs about-text">These cases are perfectly simple and easy to distinguish. In a free hour, when our power of choice when nothing prevents our being able to do what we like best, every pleasure is to be welcomed and every pain avoided. Ut enim ad minim veniam, quis nostrud exercitation. Duis aute irure dolor in reprehen derit in voluptate velit esse cillum dolore eu fugiat nulla pariatur.</p>

<!-- cases -->
<div class="abs cases" role="img" aria-label="Dark background photo of a courtroom with scales of justice"></div>
<div class="abs label" style="top:998px">Cases We Handle</div>
<h2 class="abs serif cases-title">We Are Here To Fight Against Any<br>Violance With <span class="gold">Experience</span></h2>
<div class="abs divider"></div>

<div class="abs card" style="left:193px;top:1149px">
  <svg width="34" height="30" viewBox="0 0 34 30" fill="none" stroke="#b39b63" stroke-width="1.5"><circle cx="11" cy="8" r="5"/><circle cx="23" cy="8" r="5"/><path d="M2 29v-6a9 9 0 0 1 18 0v6M14 29v-6a9 9 0 0 1 18 0v6"/></svg>
  <h3>Family Law</h3>
  <p>It focuses on issues involving family relationships. Like adoption, divorce, child custody etc.</p>
  <div class="more">Read More →</div>
</div>
<div class="abs card photo-card" style="left:472px;top:1149px" role="img" aria-label="Photo of lawyers talking in an office corridor">
  <svg width="34" height="30" viewBox="0 0 34 30" fill="none" stroke="#c9ae6e" stroke-width="1.5"><circle cx="17" cy="5" r="4"/><path d="M17 9v20M10 14h14"/></svg>
  <h3>Corporate Security</h3>
  <p>Corporate Security termed as – shares, debentures, public deposits and loans from institutions.</p>
  <div class="more">Read More →</div>
</div>
<div class="abs card" style="left:750px;top:1149px">
  <svg width="34" height="30" viewBox="0 0 34 30" fill="none" stroke="#b39b63" stroke-width="1.5"><circle cx="10" cy="21" r="7"/><circle cx="24" cy="21" r="7"/><path d="M10 14l4-10h6l4 10"/></svg>
  <h3>Criminal Law</h3>
  <p>A misdemeanor is a lower level of crime, while a felony is involved in more serious offences.</p>
  <div class="more">Read More →</div>
</div>
<div class="abs card" style="left:193px;top:1378px">
  <svg width="34" height="30" viewBox="0 0 34 30" fill="none" stroke="#b39b63" stroke-width="1.5"><rect x="6" y="1" width="18" height="26"/><path d="M10 8h10M10 13h10M10 18h6M22 24l9-11"/></svg>
  <h3>Bankruptcy Law</h3>
  <p>Filing bankruptcy with a court is the first step. Anyone can file but, not everyone qualifies.</p>
  <div class="more">Read More →</div>
</div>
<div class="abs card" style="left:472px;top:1378px">
  <svg width="34" height="30" viewBox="0 0 34 30" fill="none" stroke="#b39b63" stroke-width="1.5"><path d="M3 28V14l10-7 10 7v14M23 28V8h8v20M1 28h32M9 18h3M14 18h3M9 23h3M14 23h3"/></svg>
  <h3>Real Estate Law</h3>
  <p>Property law is the area of law that governs the various forms of ownership and tenancy in real.</p>
  <div class="more">Read More →</div>
</div>
<div class="abs card won-card" style="left:750px;top:1378px" role="img" aria-label="Photo of a gavel and scales of justice on a desk">
  <svg width="34" height="34" viewBox="0 0 34 34" fill="none" stroke="#fff" stroke-width="1.5" style="margin-top:66px"><circle cx="17" cy="17" r="15"/><path d="M13 10l10 7-10 7z"/></svg>
  <h3 style="margin-top:8px">Cases Won</h3>
</div>
<div class="abs cases-rule"></div>

<!-- experience -->
<div class="abs exp"></div>
<div class="abs exp-fade" role="img" aria-label="Faint photo of law books and a gavel"></div>
<div class="abs band"></div>
<div class="abs exp-label">Devloping Expertise</div>
<h2 class="abs serif exp-title">20 Years of Experience In<br>Various Cases</h2>
<p class="abs exp-text">These cases are perfectly simple and easy to distinguish. In a free hour, when our power of choice when nothing prevents our being able to do what we like best, every plea</p>
<ul class="abs ticks" style="left:167px;top:2005px;width:180px">
  <li>Acquire live chat enables sales</li>
  <li>Engage - marketing automation</li>
  <li>Acquire live chat enables sales</li>
  <li>Engage - marketing automation</li>
</ul>
<ul class="abs ticks" style="left:381px;top:2005px;width:190px">
  <li>Learn from customer feedback</li>
  <li>Support -customer support</li>
  <li>Learn from customer feedback</li>
  <li>Support -customer support</li>
</ul>
<div class="abs portrait" role="img" aria-label="Portrait photo of the attorney"></div>

<!-- contact -->
<div class="abs contact-bg" role="img" aria-label="Dark photo of a Lady Justice statue"></div>
<div class="abs contact-panel"></div>
<div class="abs contact-label">CONTACT US</div>
<h2 class="abs serif contact-title">Feel Free To Ask Send<br>Your <span class="gold">Message.</span></h2>
<p class="abs contact-text">These cases are perfectly simple and easy to distinguish.<br>In a free hour, when our power of choice when no</p>
<div class="abs field" style="left:562px;top:2487px;width:245px;height:40px">First Name</div>
<div class="abs field" style="left:832px;top:2487px;width:246px;height:40px">Last Name</div>
<div class="abs field" style="left:562px;top:2546px;width:245px;height:40px">Email</div>
<div class="abs field" style="left:832px;top:2546px;width:246px;height:40px">Cell Phone</div>
<div class="abs field" style="left:562px;top:2603px;width:516px;height:118px">Message</div>
<div class="abs btn-gold submit">Submit Request</div>

<!-- footer -->
<div class="abs footer"></div>
<div class="abs f-brand"><span class="f-mark"></span><div>DORIAN KESSLY LAW<small>A PROFESSIONAL CORPORATION</small></div></div>

<div class="abs f-item" style="left:152px;top:2942px">
  <svg width="14" height="16" viewBox="0 0 24 24" fill="none" stroke="#c0392b" stroke-width="2"><path d="M12 22s7-7 7-12a7 7 0 0 0-14 0c0 5 7 12 7 12z"/><circle cx="12" cy="10" r="2.5"/></svg>
  <div>4127 Corvel Street, Alder Point<br>Sacramento, CA</div>
</div>
<div class="abs f-item" style="left:152px;top:3005px">
  <svg width="16" height="16" viewBox="0 0 24 24" fill="none" stroke="#c0392b" stroke-width="2"><path d="M3 4h18v13H8l-5 4z"/></svg>
  <div>Tell Us The Reason For Your Query<br><b>info@example.com</b></div>
</div>
<div class="abs f-item" style="left:152px;top:3068px">
  <svg width="16" height="16" viewBox="0 0 24 24" fill="none" stroke="#c0392b" stroke-width="2"><circle cx="12" cy="12" r="9"/><path d="M12 7v5l3 2"/></svg>
  <div>Monday To Sataraday : 8am - 6pm.<br>Sunday CLOSED</div>
</div>
<div class="abs badge"></div>

<div class="abs serif f-head" style="left:458px;top:2869px">Contact Info</div>
<div class="abs f-underline" style="left:458px;top:2899px"></div>
<div class="abs f-item" style="left:458px;top:2919px;width:290px">We are always available for you to pass &amp; get back on the right track.</div>
<div class="abs f-item" style="left:458px;top:2998px">
  <svg width="14" height="16" viewBox="0 0 24 24" fill="none" stroke="#c0392b" stroke-width="2"><path d="M12 22s7-7 7-12a7 7 0 0 0-14 0c0 5 7 12 7 12z"/><circle cx="12" cy="10" r="2.5"/></svg>
  <div>4127 Corvel Street, Alder Point<br>Sacramento, CA</div>
</div>
<div class="abs f-item" style="left:458px;top:3062px">
  <svg width="16" height="16" viewBox="0 0 24 24" fill="none" stroke="#c0392b" stroke-width="2"><path d="M3 4h18v13H8l-5 4z"/></svg>
  <div>Tell Us The Reason For Your Query<br><b>info@example.com</b></div>
</div>
<div class="abs f-item" style="left:458px;top:3125px">
  <svg width="16" height="16" viewBox="0 0 24 24" fill="none" stroke="#c0392b" stroke-width="2"><circle cx="12" cy="12" r="9"/><path d="M12 7v5l3 2"/></svg>
  <div>Monday To Sataraday : 8am - 6pm.<br>Sunday CLOSED</div>
</div>
<div class="abs" style="left:458px;top:3192px;display:flex;gap:10px;align-items:center;font-size:23px">
  <svg width="36" height="32" viewBox="0 0 24 24" fill="none" stroke="#c0392b" stroke-width="2"><path d="M3 17v-5a9 9 0 0 1 18 0v5"/><rect x="2" y="15" width="4" height="7" rx="1"/><rect x="18" y="15" width="4" height="7" rx="1"/></svg>
  + 1-916-555-0148
</div>

<div class="abs serif f-head" style="left:765px;top:2869px">Quick Links</div>
<div class="abs f-underline" style="left:765px;top:2899px"></div>
<div class="abs f-link" style="left:765px;top:2936px;color:#c0392b">Make Appointment</div>
<div class="abs f-link" style="left:765px;top:2968px">Customer Services</div>
<div class="abs f-link" style="left:765px;top:3001px">Real Estate Law</div>
<div class="abs f-link" style="left:765px;top:3033px">Harassment Law</div>
<div class="abs f-link" style="left:922px;top:2936px">Criminal Case</div>
<div class="abs f-link" style="left:922px;top:2968px">Family Law</div>
<div class="abs f-link" style="left:922px;top:3001px">Bankruptcy Law</div>
<div class="abs f-link" style="left:922px;top:3033px">Personal Issues</div>

<div class="abs serif f-head" style="left:765px;top:3089px">Newsletter</div>
<div class="abs f-underline" style="left:765px;top:3119px"></div>
<div class="abs f-item" style="left:765px;top:3139px;width:285px">Subscribe to our newsletter to receive latest news &amp; notification on our services.</div>
<div class="abs" style="left:765px;top:3192px;width:240px;height:34px;background:#252e4b;font-size:9.5px;color:#6f7690;padding:11px 12px">Enter Email Address Here...</div>
<div class="abs" style="left:1005px;top:3192px;width:45px;height:34px;background:var(--gold);display:flex;align-items:center;justify-content:center">
  <svg width="14" height="11" viewBox="0 0 24 18" fill="none" stroke="#fff" stroke-width="2"><rect x="1" y="1" width="22" height="16"/><path d="M1 1l11 9 11-9"/></svg>
</div>

<div class="abs" style="left:150px;top:3300px;font-size:11px;color:var(--muted)">Copyright © 2022 By Dorian Kessly</div>
<div class="abs" style="left:150px;top:3322px;font-size:11px">About Us &nbsp;| &nbsp;Services &nbsp;| &nbsp;Privacy</div>
<div class="abs social" style="left:958px"></div>
<div class="abs social" style="left:992px"></div>
<div class="abs social" style="left:1025px"></div>

</body>
</html>
```